Stylish but eye catching vehicle signage for a Building and Carpentry business based in Sydney.**

We need vehicle signage for our White 2013 KR Halvane Van. We are not looking for a full wrap just signage that is eye catching, and memorable. Although we are a construction business our branding and Logo is sophisticated and clean and had a modern design . We would like to have vehicle branding that is consistent with that .

Our Logo is in grey and we would like to keep the design eye catching without using bright colours, we are not opposed to colour , we have used greys and ocre (brownish yellow)is our branding and would consider designs using these colours.

We would like to see designs that are stylish and sophisticated and not ones featuring tools or equipment for construction . We would like to see designs that portray our skills in the field of design .

Below I will attach our full logo and some examples of vehicle signage we like.
We would like the logo and contact details (email address and mobile number) on the sides and back.
We would also like the description
' new builds I renovations I residential I commercial '
at the bottom of the sides of the car between the wheels.
Updates

Hi Designers The contact details we would like on the vehicle are: 0491 358 064 rdeacyconstruction@postvane.net Just those two. Thanks

Target Market(s)

We would like to attract clients that are looking for quality work done right and professionally , and are happy to pay for good quality.

Contact Information for Business Card

I would like to go for a business card design that will accomodate embossing .
I would like the full logo on the front of the business card , no contact infomation.
The house or building icon in our logo will be raised or embossed by the printing company, so the back or the card will show the icon debossed (indented) .
On the back of the business card I would like the contact person's details:
ROWAN DEACY
carpenter
project manager
....and also the email address and mobile number on the back too.

Font styles to use
Sans Serif
Other font styles liked:
• Futura Lt Bt

Colors

Designer to choose only greyscale colors for use in the design.

Requirements
Must have
• Our logo (big and clear) and mobile number and email address on both sides and the back
Nice to have
• Designs or patterns that look architectural and elegant.
Should not have
• Any construction tools or equipment .
Designs like flames or lightning bolts
Too much colour or very bright colours

```html
<!DOCTYPE html>
<html lang="en">
<head>
<meta charset="utf-8">
<title>R Deacy Construction — Business Card</title>
<link href="https://fonts.googleapis.com/css2?family=Jost:wght@300;400;500&display=swap" rel="stylesheet">
<style>
  :root {
    --stage: #4a4a4c;
    --card-light: #f2f2f2;
    --card-dark: #6e6e70;
    --ink: #5a5a5c;
    --ink-soft: #8a8a8c;
    --mark: #5b5b5d;
    --paper-text: #ffffff;
  }
  * { box-sizing: border-box; margin: 0; padding: 0; }
  html, body {
    width: 1200px; height: 918px; overflow: hidden;
    background: var(--stage);
    font-family: "Jost", "Futura", sans-serif;
  }
  .stage {
    width: 1200px; height: 918px;
    display: flex; flex-direction: column; align-items: center; justify-content: center;
    gap: 44px;
  }
  .card {
    position: relative;
    width: 640px; height: 366px;
    border-radius: 4px;
    overflow: hidden;
    box-shadow: 0 14px 30px rgba(0,0,0,.35);
  }

  /* Front */
  .card--front {
    background: radial-gradient(ellipse 70% 80% at 40% 70%, var(--card-light) 0%, #d4d4d5 45%, var(--card-dark) 100%);
  }
  .brand {
    position: absolute; left: 50%; top: 78px; transform: translateX(-50%);
    display: flex; flex-direction: column; align-items: center;
    color: var(--ink);
  }
  .brand__square {
    width: 70px; height: 70px; border-radius: 14px;
    background: var(--mark);
    margin-bottom: 22px;
  }
  .brand__name {
    font-weight: 300; font-size: 38px; letter-spacing: 2px; line-height: 1;
    white-space: nowrap;
  }
  .brand__rule { width: 300px; height: 1px; background: var(--ink-soft); margin: 9px 0 5px; }
  .brand__tagline {
    font-weight: 300; font-size: 12.5px; letter-spacing: 1.6px; text-transform: uppercase;
  }
  .brand__rule--lower { margin: 5px 0 0; }

  /* Back */
  .card--back { background: var(--card-light); }
  .card__art {
    position: absolute; inset: 0;
    background: linear-gradient(155deg, #f4f4f4 0%, #d2d2d3 45%, #9a9a9c 75%, #767678 100%);
  }
  .contact {
    position: absolute; left: 52px; top: 44px;
    display: flex; align-items: center; gap: 16px;
  }
  .contact__square {
    width: 34px; height: 34px; border-radius: 7px;
    background: var(--mark);
  }
  .contact__details {
    border-left: 1px solid var(--ink-soft);
    padding-left: 12px;
    color: var(--ink); font-weight: 300; font-size: 14px; line-height: 1.45;
  }
  .person {
    position: absolute; right: 40px; bottom: 40px;
    border-left: 1px solid rgba(255,255,255,.85);
    padding-left: 12px;
    color: var(--paper-text); font-size: 17px; line-height: 1.3;
  }
  .person__name { font-weight: 500; letter-spacing: .5px; }
  .person__role { font-weight: 300; }
</style>
</head>
<body>
<main class="stage">

  <section class="card card--front" aria-label="Business card front">
    <div class="brand">
      <div class="brand__square"></div>
      <div class="brand__name">R DEACY CONSTRUCTION</div>
      <div class="brand__rule"></div>
      <div class="brand__tagline">Building and Carpentry</div>
      <div class="brand__rule brand__rule--lower"></div>
    </div>
  </section>

  <section class="card card--back" aria-label="Business card back">
    <div class="card__art" role="img" aria-label="Grey architectural panel artwork in soft silver tones"></div>

    <div class="contact">
      <div class="contact__square"></div>
      <div class="contact__details">
        <div>0491 358 064</div>
        <div>rdeacyconstruction@postvane.net</div>
      </div>
    </div>

    <div class="person">
      <div class="person__name">ROWAN DEACY</div>
      <div class="person__role">carpenter</div>
      <div class="person__role">project manager</div>
    </div>
  </section>

</main>
</body>
</html>
```